Institutional website for an IT Consulting company

Web design + HTML + CSS / Bootstrap + JS (interaction) integration in order to extend our existing website brisklane.coop.
Our website is currently aiming only for recruitment and not for customers, we want to provide a fluid transition between customer side website (this project) and recruitment website (existing site).

Ideally we would love the new design to be "inspired" by our actual graphic chart (Colors mainly). It should provide a great user experience and a landing page (or any mean) allowing the visitor to easily switch from the end customer front end (this project), the recruitment front end (existing front end https://www.brisklane.coop/) and the existing member front end (an other existing front end dedicated to members already existing).

In attachment you will find the expected site content mainly a one page with a first level of information and "link" to sub pages (a way to directly access this sub pages should also be provided).

The website should be accessible on mobile device and desktop.

The attachment is in french as it reflect the final site content, but if google translate isn't sufficient to have a general idea of the content, feel free to ask. We would love to have some visual representation for some categories.

Target Market(s)

fortune 500 companies

Industry/Entity Type

It Company

Coding

Coded - Design and coding required

Number of Pages Required

5+ page

Requirements
Must have
• This project must have an easy way to navigate between 3 sub sites, the customer one (the one designed here), the consultant / recruitment one (the existing one at brisklane.coop), the members one.

A one page experience at first leading to detail pages.

Custom made visuals to illustrate each categories.

Inspiration websites : plovu[.]fr ; tarnsby[.]com ; qolvari[.] com ...

Be inspired by the existing color from our logo and existing website at brisklane[.]coop

```html
<!DOCTYPE html>
<html lang="en">
<head>
<meta charset="utf-8">
<title>Brisklane.coop — Experts in their field</title>
<link rel="stylesheet" href="https://fonts.googleapis.com/css2?family=Montserrat:wght@500;600;700;800&family=Open+Sans:ital,wght@0,400;0,600;1,400&display=swap">
<style>
:root{
  --teal:#10b5c1;
  --teal-deep:#0ca8b5;
  --ink:#0d3b3a;
  --dark:#262626;
  --text:#6b6b6b;
  --line:#d8d8d8;
  --white:#ffffff;
}
*{margin:0;padding:0;box-sizing:border-box}
html,body{width:1200px;height:2366px;overflow:hidden;background:var(--white)}
body{position:relative;font-family:"Open Sans",Arial,sans-serif;color:var(--text)}

/* header */
.site-header{position:absolute;left:0;top:0;width:1200px;height:121px;background:var(--white);box-shadow:0 2px 6px rgba(0,0,0,.06);z-index:2}
.brand{position:absolute;font-family:"Montserrat",Arial,sans-serif;font-weight:800;color:var(--ink);line-height:1;display:flex;align-items:flex-end;gap:4px}
.brand .name{font-size:42px;letter-spacing:.5px}
.brand .tld{font-size:19px;color:var(--ink);padding-bottom:2px}
.brand .mark{width:14px;height:14px;background:var(--teal);margin-bottom:6px}
.util-nav{position:absolute;right:113px;top:15px;font-family:"Montserrat",Arial,sans-serif;font-weight:500;font-size:16px;color:var(--dark);display:flex;gap:12px;align-items:center}
.util-nav svg{vertical-align:-2px;margin-right:6px}
.main-nav{position:absolute;right:113px;top:50px;display:flex;gap:17px}
.btn{font-family:"Montserrat",Arial,sans-serif;font-weight:600;font-size:15.5px;height:49px;padding:0 15px;display:flex;align-items:center;border:2px solid #9a9a9a;color:#555}
.btn.solid{background:var(--dark);border-color:var(--dark);color:var(--white);padding:0 14px}

/* hero */
.hero{position:absolute;left:0;top:121px;width:1200px;height:405px;overflow:hidden;
  background:linear-gradient(90deg,#eef0ee 0%,#e9ecea 35%,#cfd8dc 55%,#6b7e8e 72%,#2d3c55 82%,#8fb0b4 100%)}
.hero-photo{position:absolute;inset:0}
.hero h1{position:absolute;left:112px;top:108px;font-family:"Montserrat",Arial,sans-serif;font-weight:700;color:var(--dark);line-height:1}
.hero h1 .l1{display:block;font-size:51px}
.hero h1 .l2{display:block;font-size:70px;margin-top:22px}
.dots{position:absolute;left:549px;top:344px;display:flex;gap:9px}
.dots span{width:18px;height:18px;border-radius:50%;border:2px solid #555}
.dots span.on{background:#555}

/* about */
.frame{position:absolute;left:111px;top:601px;width:425px;height:419px;background:var(--teal)}
.frame-inner{position:absolute;left:25px;top:24px;width:376px;height:371px;background:var(--white)}
.frame-photo{position:absolute;left:13px;top:13px;width:349px;height:344px;background:linear-gradient(135deg,#4a4a4f 0%,#d9d4cc 40%,#efece6 60%,#8a7563 100%)}
.about-copy{position:absolute;left:576px;top:596px;width:518px;font-size:14.8px;line-height:27.5px}
.about-copy p{margin-bottom:27px}
.ticks{list-style:none}
.ticks li{position:relative;padding-left:30px;margin-bottom:27px}
.ticks svg{position:absolute;left:0;top:6px}

/* testimonials */
.testimonials{position:absolute;left:0;top:1431px;width:1200px;height:512px;background:var(--teal-deep)}
.testimonials .tint{position:absolute;left:791px;top:0;width:409px;height:512px;background:var(--teal)}
.testimonials h2{position:absolute;left:0;right:0;top:54px;text-align:center;font-family:"Montserrat",Arial,sans-serif;font-weight:700;font-size:44px;color:var(--white)}
.client-name{position:absolute;left:110px;top:192px;width:240px;font-family:"Montserrat",Arial,sans-serif;font-weight:700;font-size:34px;line-height:44px;color:var(--white)}
.client-text{position:absolute;left:384px;top:149px;width:716px;font-size:17.2px;line-height:31px;color:var(--white)}
.divider{position:absolute;left:110px;top:302px;width:977px;height:1px;background:rgba(255,255,255,.35)}
.avatar{position:absolute;left:108px;top:328px;width:120px;height:120px;border-radius:50%;background:linear-gradient(160deg,#f4f4f4,#c9b4a3 60%,#6c6a70)}
.person{position:absolute;left:256px;top:360px;font-size:20px;line-height:31px;color:var(--white)}
.quote{position:absolute;left:385px;top:339px;width:716px;font-style:italic;font-size:16.8px;line-height:28px;color:var(--white)}
.arrows{position:absolute;left:1028px;top:1860px;display:flex;gap:7px}

/* footer */
.foot-col{position:absolute;top:1990px}
.foot-col h3{font-family:"Montserrat",Arial,sans-serif;font-weight:500;font-size:19.5px;color:#444;margin-bottom:9px}
.foot-col ul{list-style:none;font-size:15px;line-height:26.6px}
.find li{display:flex;gap:10px;align-items:flex-start}
.find li svg{margin-top:6px;flex:none}
.rule{position:absolute;left:110px;top:2272px;width:977px;height:1px;background:var(--line)}
.copyright{position:absolute;left:110px;top:2303px;font-size:15.5px}
.social{position:absolute;left:945px;top:2293px;display:flex;gap:4px}
.social span{width:44px;height:44px;border-radius:50%;border:1.5px solid #9a9a9a;display:flex;align-items:center;justify-content:center}
.social span i{width:8px;height:8px;border-radius:50%;background:var(--teal)}
</style>
</head>
<body>

<header class="site-header">
  <div class="brand" style="left:110px;top:32px"><span class="name">BRISKLANE</span><span class="mark"></span><span class="tld">.COOP</span></div>
  <nav class="util-nav">
    <span><svg width="14" height="14" viewBox="0 0 14 14"><path d="M2 12 L3 9 L10 2 L12 4 L5 11 Z" fill="#10b5c1"/></svg>REGISTER</span><span>|</span>
    <span><svg width="11" height="14" viewBox="0 0 11 14"><rect x="1" y="6" width="9" height="7" fill="#10b5c1"/><path d="M3 6 V4 a2.5 2.5 0 0 1 5 0 V6" stroke="#10b5c1" stroke-width="1.6" fill="none"/></svg>LOG IN</span><span>|</span>
    <span><svg width="14" height="14" viewBox="0 0 14 14"><circle cx="7" cy="7" r="6.5" fill="#10b5c1"/><text x="7" y="11" font-size="10" font-weight="700" text-anchor="middle" fill="#fff" font-family="Arial">?</text></svg>HELP</span>
  </nav>
  <nav class="main-nav">
    <a class="btn">I AM BRISKLANE</a>
    <a class="btn">I WISH TO JOIN BRISKLANE</a>
    <a class="btn solid">CONTACT US</a>
  </nav>
</header>

<section class="hero">
  <div class="hero-photo" role="img" aria-label="Bearded consultant in a navy suit reading a tablet in a bright office"></div>
  <h1><span class="l1">EXPERTS IN</span><span class="l2">THEIR FIELD</span></h1>
  <div class="dots"><span class="on"></span><span></span><span></span><span></span></div>
</section>

<section class="about">
  <div class="frame"><div class="frame-inner"><div class="frame-photo" role="img" aria-label="Team members' hands over printed charts on a meeting table"></div></div></div>
  <div class="about-copy">
    <p>Combining junior experiences to more than 15 years of data projects in Corvane's environments, Brisklane is able to take over all the standard steps of a MOE project. With half certified consultants on 35 different certifications, Brisklane has a great added value on all data platform issues encountered in Corvane tools. Operational on cost–plus contracts for long –term missions as well as punctual audit contracts, we provide support to product deployment such as Lumetric.</p>
    <p>The Datalys agreements, and specially the recognition of CCT valuate our skills on training your staff and the funding opportunities of these trainings.</p>
    <p>Last particular aspect, our reseller Corvane CRP status allows us to provide Corvane C365 licences and Skyvault consumption credit, while providing support in data deployment on these infrastructure. With a specific monitoring of your licences, whether you have 10 or 1 000 users, feel free to contact us on our CRP program @</p>
    <p>Our commercial and administrative team is also at your service, but also to SfE in order to assist them on daily tasks.</p>
    <ul class="ticks">
      <li><svg width="15" height="15" viewBox="0 0 15 15"><circle cx="7.5" cy="7.5" r="7.5" fill="#10b5c1"/><path d="M4 7.8 L6.5 10 L11 5" stroke="#fff" stroke-width="1.8" fill="none"/></svg>Elise and xx for all the trade agreements, prospection, information about our business structure and our skills. @<br>Pictures, Name, mail, phone</li>
      <li><svg width="15" height="15" viewBox="0 0 15 15"><circle cx="7.5" cy="7.5" r="7.5" fill="#10b5c1"/><path d="M4 7.8 L6.5 10 L11 5" stroke="#fff" stroke-width="1.8" fill="none"/></svg>Nadia, in addition of being in the co–stewardship, she also in control of all the administrative and contractual aspects, internally and for you. @ Picture, Name, mail, phone</li>
    </ul>
  </div>
</section>

<section class="testimonials">
  <div class="tint"></div>
  <h2>CLIENT TESTIMONIALS</h2>
  <div class="client-name">Quellon</div>
  <p class="client-text">Nemo enim ipsam voluptatem quia voluptas sit aspernatur aut odit aut fugit, sed quia csequ untur magni dolores eos qui ratione voluptatem sequi nesciunt. Neque porro quisquam est, qui dolorem ipsum quia dolor sit amet, consectetur, adipisci velit, sed quia non num&nbsp; eimodi tempora incidunt ut labore et dolore magnam aliquam..</p>
  <div class="divider"></div>
  <div class="avatar" role="img" aria-label="Portrait of the client testimonial author"></div>
  <div class="person">Paul Mervin<br>CEO</div>
  <p class="quote">“Nam libero tempore, cum soluta nobis est eligendi opticum que nihil impedit quo minus id quod maxime placeat facere possimus, omnis voluptas assumenda est, omnis dolor rep ellendu autem quibusdam et aut .”</p>
</section>
<div class="arrows">
  <svg width="24" height="24" viewBox="0 0 24 24"><circle cx="12" cy="12" r="12" fill="#fff"/><path d="M14 6 L8 12 L14 18" stroke="#0ca8b5" stroke-width="3" fill="none"/></svg>
  <svg width="24" height="24" viewBox="0 0 24 24"><circle cx="12" cy="12" r="12" fill="#fff"/><path d="M10 6 L16 12 L10 18" stroke="#0ca8b5" stroke-width="3" fill="none"/></svg>
</div>

<footer>
  <div class="brand" style="left:110px;top:2072px"><span class="name">BRISKLANE</span><span class="mark"></span><span class="tld">.COOP</span></div>
  <div class="foot-col" style="left:468px"><h3>Information</h3>
    <ul><li>About us</li><li>Team</li><li>Jobs</li><li>Hurry</li><li>Freelancing news</li><li>Data protection</li><li>Help</li><li>Sitemap</li></ul></div>
  <div class="foot-col" style="left:674px"><h3>Quick Links</h3>
    <ul><li>Offers and prices</li><li>Company</li><li>Open Brisklane coop</li><li>Insights</li><li>Create my Profile</li></ul></div>
  <div class="foot-col find" style="left:879px"><h3>Find Us</h3>
    <ul>
      <li><svg width="10" height="15" viewBox="0 0 10 15"><path d="M5 0 a5 5 0 0 1 5 5 c0 4 -5 10 -5 10 s-5 -6 -5 -10 a5 5 0 0 1 5 -5z" fill="#10b5c1"/><circle cx="5" cy="5" r="2" fill="#fff"/></svg><span>24 Rue des Tanneurs<br>75011 Paris</span></li>
      <li style="margin-top:26px"><svg width="14" height="14" viewBox="0 0 14 14"><path d="M3 1 L5.5 4 L4 6 C5 8 6 9 8 10 L10 8.5 L13 11 L11 13.5 C5 13 1 9 0.5 3 Z" fill="#10b5c1"/></svg><span>01 40 27 63 15</span></li>
      <li style="margin-top:28px"><svg width="17" height="12" viewBox="0 0 17 12"><rect width="17" height="12" fill="#10b5c1"/><path d="M0 0 L8.5 7 L17 0" stroke="#fff" stroke-width="1.4" fill="none"/></svg><span>contact@brisklane.coop</span></li>
    </ul></div>
  <div class="rule"></div>
  <div class="copyright">© 2020, Brisklane.coop.</div>
  <div class="social"><span aria-label="Social network one"><i></i></span><span aria-label="Social network two"><i></i></span><span aria-label="Social network three"><i></i></span></div>
</footer>

</body>
</html>
```